Travel Company is looking for a STAND OUT Business Card

I need a unique Business Card that will truly stand out. Nothing too busy. Simple is good, right? Not looking for a standard design either. No cookie cutter layout. We are a Travel Company that works more with Companies than Travelers. I had an idea to focus and emphasis on the 2 logo a bit more. This is not necessary, however thought it would look interesting. I am just looking for something interesting and a bit different. Does't have to completely off the wall crazy, just not your run of the mill business card.

Target Market(s)

Hoteliers, Resort Management, Call Centers, Executives, Travelers, Families, Businesses

Industry/Entity Type

Hospitality

Contact Information for Business Card

President/CEO - Marcus T Bellamy (title not necessary if design doesn't allow for it)
contact - (407) 555-0186
email - mbellamy@wayfarenow.example
address - 4812 Quillmore Ave #164
Orlando, FL 32804
website - www.wayfarenow.example

Font styles to use
Serif
Other font styles liked:
• Avenir Next LT Pro BOLD

Requirements
Must have
• simple look and design. Unique design
Nice to have
• I attached the 2 logo separate from the main logo. This can be used separately from the Main Logo, together with the main logo or as main logo. I included the logo font. Use it or not, designers choice.
Should not have
• cookie cutter design. Little use of red other than the logo

```html
<!DOCTYPE html>
<html lang="en">
<head>
<meta charset="utf-8">
<title>Wayfare Now – Business Card</title>
<link rel="stylesheet" href="https://fonts.googleapis.com/css2?family=Arimo:wght@400;700&display=swap">
<style>
  :root {
    --backdrop: #3b3b3d;
    --card-white: #ffffff;
    --card-black: #0d0d0d;
    --brand-red: #e3141b;
    --ink: #111111;
    --muted: #5a5a5a;
  }
  * { box-sizing: border-box; margin: 0; padding: 0; }
  html, body {
    width: 1200px;
    height: 843px;
    overflow: hidden;
  }
  body {
    background: var(--backdrop);
    font-family: "Arimo", Arial, sans-serif;
    display: flex;
    flex-direction: column;
    align-items: center;
    justify-content: center;
    gap: 40px;
  }
  .card {
    position: relative;
    width: 620px;
    height: 354px;
    overflow: hidden;
    box-shadow: 0 10px 24px rgba(0,0,0,0.45);
  }
  .card--front { background: var(--card-white); }
  .card--back {
    background: var(--card-black);
    display: flex;
    align-items: center;
    justify-content: center;
  }

  .brand-band {
    position: absolute;
    left: 400px;
    top: 0;
    width: 112px;
    height: 150px;
    background: var(--brand-red);
  }
  .brand-name {
    position: absolute;
    left: 330px;
    top: 92px;
    width: 252px;
    text-align: center;
    font-weight: 700;
    font-size: 38px;
    letter-spacing: -0.5px;
    color: var(--ink);
  }
  .card--back .brand-name {
    position: static;
    width: auto;
    color: var(--card-white);
    font-size: 44px;
  }

  .holder {
    position: absolute;
    left: 40px;
    top: 118px;
  }
  .holder__name {
    color: var(--brand-red);
    font-size: 19px;
    font-weight: 700;
    letter-spacing: 0.2px;
  }
  .holder__title {
    margin-top: 5px;
    color: var(--ink);
    font-size: 14px;
  }

  .contact-list {
    position: absolute;
    left: 40px;
    top: 184px;
    list-style: none;
  }
  .contact-list li {
    display: flex;
    align-items: center;
    gap: 9px;
    height: 22px;
    color: var(--muted);
    font-size: 13px;
  }
  .contact-list svg { width: 12px; height: 12px; flex: none; }

  .divider {
    position: absolute;
    left: 306px;
    top: 186px;
    width: 1px;
    height: 74px;
    background: var(--brand-red);
  }
  .address {
    position: absolute;
    left: 324px;
    top: 222px;
    font-style: normal;
    color: var(--muted);
    font-size: 13px;
    line-height: 20px;
  }
</style>
</head>
<body>

  <section class="card card--front" aria-label="Business card front">
    <div class="brand-band"></div>
    <div class="brand-name">Wayfare Now</div>

    <div class="holder">
      <p class="holder__name">Marcus T Bellamy</p>
      <p class="holder__title">President/CEO</p>
    </div>

    <ul class="contact-list">
      <li>
        <svg viewBox="0 0 12 12" aria-hidden="true"><path fill="#e3141b" d="M2.5 0.8l1.8-0.3 1 2.6-1.2 0.9c0.6 1.3 1.6 2.3 2.9 2.9l0.9-1.2 2.6 1-0.3 1.8C9.5 9.9 8.6 10.4 7.6 10.2 4.3 9.4 2.6 7.7 1.8 4.4 1.6 3.4 2.1 2.5 2.5 0.8z"/></svg>
        (407) 555-0186
      </li>
      <li>
        <svg viewBox="0 0 12 12" aria-hidden="true"><rect x="0.5" y="2" width="11" height="8" fill="#e3141b"/><path d="M0.8 2.4L6 6.6l5.2-4.2" fill="none" stroke="#fff" stroke-width="1"/></svg>
        mbellamy@wayfarenow.example
      </li>
      <li>
        <svg viewBox="0 0 12 12" aria-hidden="true"><circle cx="6" cy="6" r="5.5" fill="#e3141b"/><path d="M5 3.6l3 2.4-3 2.4z" fill="#fff"/></svg>
        www.wayfarenow.example
      </li>
    </ul>

    <div class="divider"></div>
    <address class="address">
      4812 Quillmore Ave #164<br>
      Orlando, FL 32804
    </address>
  </section>

  <section class="card card--back" aria-label="Business card back">
    <div class="brand-name">Wayfare Now</div>
  </section>

</body>
</html>
```